Business Card Design Project

We need a business card design for an existing company in Dallas/Fort Worth that is expanding services and re-branding. We are changing the name from Bristow Commercial Cleaning to Kelmont Facility Services. We are expanding from only commercial cleaning to include complete commercial landscape and facility maintenance services, too.

As stated, we offer a package of services that includes landscape, janitorial and facility services, which is largely unique in the industry.

We would like a design that communicates trust/partnership with a professional, corporate image, but not necessarily using the standard white business card. We would like a design that perhaps uses darker blues or perhaps a gray background, but we are open to other ideas. We might also be interested in a double-sided design - maybe with our logo on the back, printed on a gray background?

We will probably stick with the attached logo, but if you've got another inspired idea....

Target Market(s)

Property managers, commercial real estate professionals, corporate executives

Industry/Entity Type

Landscape

Requirements
Should not have
• Not interested in old style fonts.

```html
<!DOCTYPE html>
<html lang="en">
<head>
<meta charset="UTF-8">
<title>Kelmont Facility Services – Business Card</title>
<link href="https://fonts.googleapis.com/css2?family=Questrial&display=swap" rel="stylesheet">
<style>
  :root {
    --backdrop: #d9d6d2;
    --card-core: #0a0c3a;
    --card-edge: #000000;
    --ink: #d8d8dc;
    --ink-soft: #a9a9b3;
    --rule: #e6e6ea;
    --divider: #2a2c4a;
  }
  * { margin: 0; padding: 0; box-sizing: border-box; }
  html, body {
    width: 1200px; height: 900px; overflow: hidden;
    background: var(--backdrop);
    font-family: "Questrial", sans-serif;
  }
  .canvas { position: relative; width: 1200px; height: 900px; }
  .card {
    position: absolute;
    width: 548px; height: 304px;
    background: radial-gradient(ellipse 45% 75% at 55% 55%, var(--card-core) 0%, #04051c 55%, var(--card-edge) 100%);
    box-shadow: 0 2px 6px rgba(0,0,0,0.35);
    overflow: hidden;
  }
  .card--front { left: 340px; top: 112px; }
  .card--back  { left: 339px; top: 444px; }

  .rule { position: absolute; background: var(--rule); height: 3px; }
  .rule--low  { left: 20px; top: 163px; width: 136px; }
  .rule--high { left: 215px; top: 116px; width: 318px; }

  .brand-square { position: absolute; border: 3px solid var(--rule); }
  .card--front .brand-square { left: 162px; top: 116px; width: 50px; height: 50px; }
  .card--back .brand-square { left: 78px; top: 113px; width: 38px; height: 37px; border-width: 2px; border-color: var(--ink-soft); }

  .brand-name {
    position: absolute; color: var(--ink); font-weight: 400;
    text-transform: uppercase; line-height: 1;
  }
  .brand-name span { display: block; }
  .card--front .brand-name { left: 220px; top: 124px; }
  .card--front .brand-name .brand-main { font-size: 21px; letter-spacing: 2px; }
  .card--front .brand-name .brand-sub { font-size: 11.5px; letter-spacing: 1.6px; margin-top: 3px; }
  .card--back .brand-name { left: 121px; top: 116px; color: var(--ink-soft); }
  .card--back .brand-name .brand-main { font-size: 16px; letter-spacing: 1.5px; }
  .card--back .brand-name .brand-sub { font-size: 9px; letter-spacing: 1.2px; margin-top: 2px; }

  .divider { position: absolute; left: 273px; top: 61px; width: 1px; height: 161px; background: var(--divider); }

  .contact { position: absolute; left: 284px; top: 80px; color: var(--ink); }
  .contact-heading { font-size: 15px; letter-spacing: 0.5px; }
  .contact-name, .contact-role { font-size: 11.5px; color: var(--ink-soft); }
  .contact-name { margin-top: 7px; }
  .contact-role { margin-top: 3px; }
  .contact-web { font-size: 12.5px; margin-top: 40px; }
  .contact-phone { font-size: 12px; margin-top: 4px; }
</style>
</head>
<body>
<main class="canvas">
  <section class="card card--front" aria-label="Card front">
    <div class="rule rule--low"></div>
    <div class="brand-square"></div>
    <div class="rule rule--high"></div>
    <div class="brand-name">
      <span class="brand-main">Kelmont</span>
      <span class="brand-sub">Facility Services</span>
    </div>
  </section>

  <section class="card card--back" aria-label="Card back">
    <div class="brand-square"></div>
    <div class="brand-name">
      <span class="brand-main">Kelmont</span>
      <span class="brand-sub">Facility Services</span>
    </div>
    <div class="divider"></div>
    <div class="contact">
      <p class="contact-heading">NAME SURNAME</p>
      <p class="contact-name">Wade Hollis</p>
      <p class="contact-role">General Manager</p>
      <p class="contact-web">www.kelmontfacilityservices.com</p>
      <p class="contact-phone">000-000-0000</p>
    </div>
  </section>
</main>
</body>
</html>
```